Driving School
Brightlane Driving School
Project: Driving School
Driving School - Automotive
Creative Brief
Professional
214-52 Hollister Avenue Jamaica NY 11432
brightlanedriving@mailnest.example
www.BrightlaneDriving.example
Car & CDL Training
Calendar Or Driving school Directional MAP

```html
<!DOCTYPE html>
<html lang="en">
<head>
<meta charset="utf-8">
<title>Brightlane Driving School – Business Card</title>
<link rel="stylesheet" href="https://fonts.googleapis.com/css2?family=Montserrat:wght@400;500;600;800&display=swap">
<style>
  :root {
    --brand-blue: #2f64a8;
    --brand-blue-dark: #24508a;
    --brand-red: #d2282f;
    --card-white: #ffffff;
    --ink: #2f64a8;
    --page-bg: #e6e8eb;
  }
  * { box-sizing: border-box; margin: 0; padding: 0; }
  html, body {
    width: 1200px; height: 864px; overflow: hidden;
    background: var(--page-bg);
    font-family: "Montserrat", Arial, sans-serif;
  }
  .stage {
    position: relative; width: 1200px; height: 864px;
    display: flex; flex-direction: column; align-items: center; justify-content: center; gap: 48px;
  }
  .card {
    position: relative; width: 640px; height: 366px;
    border-radius: 18px; overflow: hidden;
    box-shadow: 0 10px 28px rgba(0,0,0,0.18);
  }
  /* Front */
  .card--front {
    background: radial-gradient(ellipse at 50% 45%, #3a74bd 0%, var(--brand-blue) 55%, var(--brand-blue-dark) 100%);
    display: flex; align-items: center; justify-content: center;
  }
  .wordmark {
    display: flex; align-items: center; gap: 14px;
    font-weight: 800; letter-spacing: -0.5px; line-height: 1;
  }
  .wordmark__dot { width: 20px; height: 20px; border-radius: 50%; background: currentColor; flex: none; }
  .card--front .wordmark { color: var(--card-white); font-size: 46px; }
  /* Back */
  .card--back { background: var(--card-white); }
  .card__curves { position: absolute; inset: 0; width: 100%; height: 100%; }
  .card--back .logo-block { position: absolute; left: 32px; top: 56px; }
  .card--back .wordmark { color: var(--brand-blue); align-items: flex-start; gap: 12px; }
  .wordmark__text { display: flex; flex-direction: column; gap: 6px; }
  .wordmark__name { font-size: 38px; }
  .wordmark__sub { font-size: 15px; letter-spacing: 3px; }
  .card--back .wordmark__dot { width: 18px; height: 18px; margin-top: 9px; }
  .logo-rule { margin-top: 12px; height: 6px; width: 246px; background: var(--brand-red); }
  .holder {
    position: absolute; left: 32px; bottom: 62px;
    font-size: 14px; font-weight: 600; letter-spacing: 2px; text-transform: uppercase; color: var(--ink);
  }
  .address {
    position: absolute; left: 32px; bottom: 32px;
    font-size: 11px; font-weight: 500; letter-spacing: 0.5px; text-transform: uppercase; color: var(--ink);
  }
  .contacts {
    position: absolute; right: 20px; top: 96px;
    list-style: none; display: flex; flex-direction: column; gap: 14px;
  }
  .contacts__item { display: flex; align-items: center; gap: 8px; font-size: 11px; font-weight: 500; color: var(--ink); white-space: nowrap; }
  .contacts__icon {
    width: 20px; height: 20px; border-radius: 50%; background: var(--brand-blue);
    display: flex; align-items: center; justify-content: center; flex: none;
  }
  .contacts__icon svg { width: 12px; height: 12px; }
</style>
</head>
<body>
<main class="stage">
  <section class="card card--front" aria-label="Card front">
    <div class="wordmark"><span class="wordmark__dot"></span><span>Brightlane</span></div>
  </section>

  <section class="card card--back" aria-label="Card back">
    <svg class="card__curves" viewBox="0 0 640 366" preserveAspectRatio="none" aria-hidden="true">
      <path d="M352 -4 C 304 110, 304 250, 384 370" fill="none" stroke="var(--brand-red)" stroke-width="5"/>
      <path d="M370 -4 C 322 110, 322 250, 404 370" fill="none" stroke="var(--brand-blue)" stroke-width="11"/>
    </svg>

    <div class="logo-block">
      <div class="wordmark">
        <span class="wordmark__dot"></span>
        <span class="wordmark__text">
          <span class="wordmark__name">Brightlane</span>
          <span class="wordmark__sub">DRIVING SCHOOL</span>
        </span>
      </div>
      <div class="logo-rule"></div>
    </div>

    <p class="holder">Dana Reyes</p>
    <p class="address">214-52 Hollister Avenue Jamaica NY 11432</p>

    <ul class="contacts">
      <li class="contacts__item">
        <span class="contacts__icon"><svg viewBox="0 0 24 24"><path fill="#fff" d="M6.6 10.8a15 15 0 0 0 6.6 6.6l2.2-2.2c.3-.3.7-.4 1-.2 1.1.4 2.3.6 3.6.6.6 0 1 .4 1 1V20c0 .6-.4 1-1 1A17 17 0 0 1 3 4c0-.6.4-1 1-1h3.5c.6 0 1 .4 1 1 0 1.3.2 2.5.6 3.6.1.3 0 .7-.2 1z"/></svg></span>
        718-555-0143
      </li>
      <li class="contacts__item">
        <span class="contacts__icon"><svg viewBox="0 0 24 24"><path fill="#fff" d="M6.6 10.8a15 15 0 0 0 6.6 6.6l2.2-2.2c.3-.3.7-.4 1-.2 1.1.4 2.3.6 3.6.6.6 0 1 .4 1 1V20c0 .6-.4 1-1 1A17 17 0 0 1 3 4c0-.6.4-1 1-1h3.5c.6 0 1 .4 1 1 0 1.3.2 2.5.6 3.6.1.3 0 .7-.2 1z"/></svg></span>
        718-555-0178
      </li>
      <li class="contacts__item">
        <span class="contacts__icon"><svg viewBox="0 0 24 24"><path fill="#fff" d="M3 6h18v12H3z"/><path fill="none" stroke="#2f64a8" stroke-width="2" d="M3 6l9 7 9-7"/></svg></span>
        brightlanedriving@mailnest.example
      </li>
      <li class="contacts__item">
        <span class="contacts__icon"><svg viewBox="0 0 24 24"><circle cx="12" cy="12" r="8" fill="none" stroke="#fff" stroke-width="2"/><path fill="none" stroke="#fff" stroke-width="2" d="M4 12h16M12 4c3 3 3 13 0 16M12 4c-3 3-3 13 0 16"/></svg></span>
        www.BrightlaneDriving.example
      </li>
    </ul>
  </section>
</main>
</body>
</html>
```